New River III Precinct 6x11 GOTV postcard

We require BOTH persuasive copy and high-impact layout for an oversized 6x11 political mailer. This might be one person, but it likely requires a specialized "creative team." of an experienced political strategist copywriter PLUS a graphic designer - so the words fit the exact layout block, and the visuals reinforce the psychological punch of the headline.

The goal is to remove all excuses a targeted audience of ~900 registered Democratic + ~1800 Unaffiliated voters in our precinct - have for not voting.

I need to be able to work by phone / online chat to iterate designs
I need to own the design in the top couple of software outputs that any printer service will require.

I want to experiment with very subtle background images as follows:
- Front of postcard that conveys "CHANGE" of not just seasons - but of encouraging change of precinct voter representation - so anything about fall foliage / conveyance of change tie-in is worthy of considering
- Back of postcard - any Appalachian long rage mountain view that includes 5-7 layers of hills in the distance.
Some photos as samples to consider.

Target Market(s)

~2,700 registered Democrats and Unaffiliated voters

Requirements
Must have
• We require BOTH persuasive copy and high-impact layout for an oversized 6x11 political mailer. This might be one person, but it likely requires a specialized "creative team." of an experienced political strategist copywriter PLUS a graphic designer - so the words fit the exact layout block, and the visuals reinforce the psychological punch of the headline
Nice to have
• subtle background photos

```html
<!DOCTYPE html>
<html lang="en">
<head>
<meta charset="utf-8">
<title>New River III Precinct 6x11 GOTV Postcard</title>
<link href="https://fonts.googleapis.com/css2?family=Anton&family=Oswald:wght@500;600;700&family=Roboto+Condensed:wght@400;500&family=Archivo+Black&display=swap" rel="stylesheet">
<style>
  :root{
    --board:#9b9b9b;
    --ink-white:#ffffff;
    --gold:#f7bd16;
    --gold-line:#e9b422;
    --navy:#2d3276;
    --navy-soft:#8088c9;
    --brown-dark:#2e1d17;
    --cream:#fdf1e2;
    --sky-blue:#9bb6d2;
    --hill-blue:#5d80ad;
    --forest:#2f4a22;
    --note:#fbeb98;
    --note-edge:#f3d45e;
    --note-ink:#1f1d18;
    --pin:#d8242a;
    --skin:#e8946c;
  }
  *{margin:0;padding:0;box-sizing:border-box}
  html,body{width:1200px;height:1066px;overflow:hidden;background:var(--board)}
  .board{position:relative;width:1200px;height:1066px}

  .side-label{position:absolute;font-family:"Archivo Black",sans-serif;color:var(--ink-white);font-size:48px;line-height:1;white-space:nowrap;transform-origin:left top;transform:rotate(-90deg);letter-spacing:1px}
  .side-label--front{left:916px;top:366px}
  .side-label--back{left:241px;top:872px}

  /* FRONT */
  .card-front{position:absolute;left:59px;top:52px;width:850px;height:468px;overflow:hidden;background:var(--brown-dark)}
  .card-front__photo{position:absolute;inset:0;background:
      radial-gradient(ellipse 170px 160px at 630px 230px,#f2a623 0%,#d98a1a 55%,rgba(120,70,30,0) 100%),
      radial-gradient(ellipse 260px 200px at 760px 60px,rgba(180,110,60,.5),rgba(0,0,0,0) 70%),
      linear-gradient(120deg,#3a2419 0%,#4b2e20 40%,#3c3532 70%,#2b2a2a 100%)}
  .issues{position:absolute;left:45px;top:36px;font-family:"Oswald",sans-serif;font-weight:700;color:var(--ink-white);font-size:18px;letter-spacing:.2px}
  .issues__row{display:flex;align-items:center;gap:14px;height:34px;margin-bottom:5px}
  .issue{display:flex;align-items:center;gap:5px;white-space:nowrap}
  .issue svg{width:33px;height:33px;flex:none}

  .headline{font-family:"Anton",sans-serif;text-transform:uppercase;font-weight:400}
  .headline__top,.headline__main{position:absolute;left:45px;line-height:1;white-space:nowrap}
  .headline__top{top:129px;color:var(--ink-white);font-size:79px;letter-spacing:6px}
  .headline__main{top:207px;color:var(--gold);font-size:106px;letter-spacing:10px}

  .subhead{position:absolute;left:51px;top:312px;display:flex;align-items:flex-end;gap:8px;font-family:"Oswald",sans-serif;font-weight:600;color:var(--ink-white);text-transform:uppercase}
  .subhead__lead{font-size:21px;line-height:1;border-bottom:3px double var(--gold-line);padding-bottom:5px;margin-bottom:2px}
  .subhead__main{font-size:35px;line-height:1}

  .vote-sign__pole{position:absolute;left:69px;top:361px;width:6px;height:107px;background:#e9792a;border:2px solid #1a1a1a;z-index:1}
  .vote-sign{position:absolute;left:26px;top:370px;width:92px;height:39px;background:var(--gold);border:3px solid #1a1a1a;border-radius:5px;font-family:"Oswald",sans-serif;font-weight:500;font-size:24px;line-height:33px;text-align:center;color:#1a1a1a;z-index:2}
  .vote-sign__hand{position:absolute;left:58px;top:414px;width:52px;height:54px;border-radius:50% 50% 0 0;background:radial-gradient(ellipse at 50% 35%,rgba(232,148,108,.75) 0%,rgba(232,148,108,.35) 55%,rgba(232,148,108,0) 100%);z-index:3}

  .cta-band{position:absolute;left:0;bottom:0;width:850px;height:56px;background:var(--navy);border-top:2px solid #c98a2a;font-family:"Anton",sans-serif;text-transform:uppercase}
  .cta-band__check{position:absolute;left:136px;top:11px;width:30px;height:30px}
  .cta-band__main{position:absolute;left:173px;top:6px;color:var(--ink-white);font-size:34px;letter-spacing:3px;line-height:40px;white-space:nowrap}
  .cta-band__tag{position:absolute;left:433px;top:14px;color:var(--navy-soft);font-size:25px;letter-spacing:2.2px;line-height:28px;white-space:nowrap}

  /* BACK */
  .card-back{position:absolute;left:299px;top:554px;width:853px;height:469px;overflow:hidden}
  .card-back__photo{position:absolute;inset:0;background:linear-gradient(180deg,var(--cream) 0%,#f4ebe4 22%,#c9d3df 35%,var(--sky-blue) 48%,var(--hill-blue) 66%,#6f8fb4 74%,#3f5e33 84%,var(--forest) 100%)}
  .stamp-box{position:absolute;left:744px;top:21px;width:86px;height:98px;background:#fff;border:1px solid #555}
  .address-box{position:absolute;left:563px;top:165px;width:267px;height:160px;background:#fff;border:1px solid #555;display:flex;align-items:center;justify-content:center;text-align:center;font-family:"Roboto Condensed",sans-serif;font-size:17px;line-height:21px;color:#111}
  .note{position:absolute;left:46px;top:33px;width:326px;height:405px;background:linear-gradient(160deg,#fdf3b4 0%,var(--note) 55%,var(--note-edge) 100%);box-shadow:0 3px 8px rgba(0,0,0,.25);border-radius:0 0 6px 30px;padding:58px 16px 0 33px;font-family:"Roboto Condensed",sans-serif;color:var(--note-ink)}
  .note__pin{position:absolute;left:168px;top:-6px;width:20px;height:20px;border-radius:50%;background:var(--pin)}
  .note__salutation{font-size:18.5px;font-weight:400;text-align:center;margin:0 0 8px -14px;letter-spacing:-.1px}
  .note p{font-size:8.1px;line-height:10.6px;margin-bottom:5px;color:var(--note-ink)}
  .note__signoff{font-size:10.5px;line-height:13px;margin-top:-3px}
  .note__voter{font-size:9px;font-weight:500;margin:11px 0 8px}
  .note__details{font-size:8.4px;line-height:12px}
  .note__details strong{font-weight:500}
  .note__rules{font-size:8.4px;line-height:12.5px;text-align:center;margin:12px 0 0 -10px}
</style>
</head>
<body>
<div class="board">

  <section class="card-front" aria-label="Postcard front">
    <div class="card-front__photo" role="img" aria-label="Background photo of a golden autumn maple leaf on dark fallen leaves"></div>

    <div class="issues">
      <div class="issues__row">
        <span class="issue"><svg viewBox="0 0 34 34"><circle cx="17" cy="17" r="15.5" fill="none" stroke="#f7bd16" stroke-width="1.6"/><rect x="10" y="15" width="4" height="9" fill="none" stroke="#fff"/><rect x="16" y="11" width="4" height="13" fill="none" stroke="#fff"/><circle cx="23.5" cy="13" r="3" fill="none" stroke="#fff"/></svg>FAMILY BUGET</span>
        <span class="issue"><svg viewBox="0 0 34 34"><circle cx="17" cy="17" r="15.5" fill="none" stroke="#f7bd16" stroke-width="1.6"/><path d="M15 10h4v5h5v4h-5v5h-4v-5h-5v-4h5z" fill="none" stroke="#fff"/></svg>HEALTH</span>
        <span class="issue"><svg viewBox="0 0 34 34"><circle cx="17" cy="17" r="15.5" fill="none" stroke="#f7bd16" stroke-width="1.6"/><path d="M17 9v16M10 12h14M10 12l-3 7h6zM24 12l-3 7h6zM13 25h8" fill="none" stroke="#fff"/></svg>REPRODUCTIVE RIGHTS</span>
        <span class="issue"><svg viewBox="0 0 34 34"><circle cx="17" cy="17" r="15.5" fill="none" stroke="#f7bd16" stroke-width="1.6"/><path d="M17 8l8 3v6c0 5-4 8-8 9-4-1-8-4-8-9v-6z" fill="none" stroke="#fff"/><path d="M14 13v8M20 13v8" stroke="#fff"/></svg>FOOD SECURITY</span>
      </div>
      <div class="issues__row">
        <span class="issue"><svg viewBox="0 0 34 34"><circle cx="17" cy="17" r="15.5" fill="none" stroke="#f7bd16" stroke-width="1.6"/><path d="M8 13l9 2 9-2v10l-9 2-9-2zM17 15v10" fill="none" stroke="#fff"/><circle cx="17" cy="9.5" r="2" fill="none" stroke="#fff"/></svg>EDUCATION</span>
        <span class="issue"><svg viewBox="0 0 34 34"><circle cx="17" cy="17" r="15.5" fill="none" stroke="#f7bd16" stroke-width="1.6"/><path d="M8 17l9-8 9 8M11 15v10h12V15M15 25v-5h4v5" fill="none" stroke="#fff"/></svg>HOUSING</span>
        <span class="issue"><svg viewBox="0 0 34 34"><circle cx="17" cy="17" r="15.5" fill="none" stroke="#f7bd16" stroke-width="1.6"/><path d="M18 8l-6 10h5l-2 8 7-11h-5z" fill="none" stroke="#fff"/></svg>ENERGY</span>
        <span class="issue"><svg viewBox="0 0 34 34"><circle cx="17" cy="17" r="15.5" fill="none" stroke="#f7bd16" stroke-width="1.6"/><circle cx="17" cy="17" r="8" fill="none" stroke="#fff"/><path d="M9 17h16M17 9c-4 4-4 12 0 16M17 9c4 4 4 12 0 16" fill="none" stroke="#fff"/></svg>ENVIRONMENT</span>
      </div>
    </div>

    <h1 class="headline">
      <span class="headline__top">Vote for</span>
      <span class="headline__main">Change</span>
    </h1>
    <div class="subhead"><span class="subhead__lead">For a</span><span class="subhead__main">New Representation</span></div>

    <div class="cta-band">
      <svg class="cta-band__check" viewBox="0 0 30 30"><circle cx="15" cy="15" r="12.5" fill="none" stroke="#f7bd16" stroke-width="3"/><path d="M9 15.5l4 4 8-8" fill="none" stroke="#f7bd16" stroke-width="3" stroke-linecap="round" stroke-linejoin="round"/></svg>
      <span class="cta-band__main">Vote Democrat</span>
      <span class="cta-band__tag">For people. For your future</span>
    </div>

    <div class="vote-sign__pole"></div>
    <div class="vote-sign">VOTE</div>
    <div class="vote-sign__hand" role="img" aria-label="Illustration of a hand gripping the vote sign pole"></div>
  </section>
  <div class="side-label side-label--front">FRONT</div>

  <section class="card-back" aria-label="Postcard back">
    <div class="card-back__photo" role="img" aria-label="Background photo of layered Appalachian blue ridges above a green forest"></div>

    <div class="note">
      <div class="note__pin" role="img" aria-label="Red push pin"></div>
      <h2 class="note__salutation">Dear New River III Neighbor</h2>
      <p>We live in a representative democracy. We expect our representatives will exercise independent thinking and support policies and legislation that don't harms - and that reflect the MAJORITY VIEWS of precinct citizens.</p>
      <p>But our current representatives HAVE STOPPED LISTENING - they are now bringing harmful policies straight to Watauga County. IT'S TIME TO HOLD THEM ACCOUNTABLE AND VOTE THEM OUT.</p>
      <p>Make no mistake: in 2026, every election is partisan. Even Judicial seats are now tied directly to state platforms.</p>
      <p>Any candidate who refuses to publicly condemn Raleigh's gerrymandered overreach into Watauga politics-or refuses to fight funding cuts for our healthcare, education, and environmental justice - is actively supporting these harmful policies.</p>
      <p>They are hoping their silence fools you. DON'T BE FOOLED. This November,</p>
      <div class="note__signoff">VOTE FOR CHANGE.</div>
      <div class="note__voter">YOU ARE A REGISTERED VOTER IN WATAUGA COUNTY</div>
      <div class="note__details">
        <strong>YOU RESIDE IN PRECINCT:</strong> NEW RIVER III<br>
        <strong>POLLING PLACES AVAILABLE TO YOU ARE:</strong> LOCATION,. 2, 3<br>
        <strong>EARLY VOTING STARTS ON:</strong><br>
        DEADLINE TO APPLY FOR MAIL-IN BALLOTS
      </div>
      <div class="note__rules">KNOW THE RULES TO ENSURE YOUR<br>MAIL-IN-BALLOT COUNTS</div>
    </div>

    <div class="stamp-box"></div>
    <div class="address-box">LOCAL POSTAL<br>CUSTOMER</div>
  </section>
  <div class="side-label side-label--back">BACK</div>

</div>
</body>
</html>
```